Flyer Design Project

Just needing a sleek, modern brochure design for my Paint Contracting business. It's a one sided leaflet (99mm X 210mm)

Brennard Finish Coatings
"Over 25 years experience"
"We set the standard for quality and service"

Call for a free estimate:
Dorian Velsher 0498153620
Dorianvelsher0@quillmail.com
http://brennardfinishcoatings.webnest.com.au/

All Painting services offered:
Interior, exterior, pressure washing, staing, roof restoration, residential, commercial and body corporate

Target Market(s)

Home owners

Industry/Entity Type

Business

```html
<!DOCTYPE html>
<html lang="en">
<head>
<meta charset="utf-8">
<title>Brennard Finish Coatings – Flyer</title>
<link href="https://fonts.googleapis.com/css2?family=Ubuntu:wght@500;700&family=Source+Sans+3:wght@400;600&display=swap" rel="stylesheet">
<style>
  :root {
    --page-bg: #e6e6e6;
    --navy-deep: #0b2a63;
    --navy-mid: #1a4591;
    --navy-light: #2f5eae;
    --white: #ffffff;
    --brand-green: #0a8a5a;
    --badge-dark: #111111;
    --badge-slate: #545e8f;
    --swatch-yellow: #f6c200;
    --swatch-orange: #e8720c;
    --swatch-red: #d64545;
    --swatch-plum: #7a3560;
    --swatch-sky: #9db8d9;
    --swatch-green: #0e9a63;
  }
  * { margin: 0; padding: 0; box-sizing: border-box; }
  html, body {
    width: 1200px; height: 900px; overflow: hidden;
    background: var(--page-bg);
  }
  .flyer {
    position: absolute; left: 50px; top: 190px;
    width: 1100px; height: 520px; overflow: hidden;
    box-shadow: 0 6px 18px rgba(0,0,0,0.25);
    font-family: "Source Sans 3", sans-serif;
    color: var(--white);
  }
  .backdrop-photo {
    position: absolute; inset: 0;
    background:
      radial-gradient(ellipse at 25% 50%, #c9a040 0%, rgba(201,160,64,0) 35%),
      radial-gradient(ellipse at 10% 70%, #b5282a 0%, rgba(181,40,42,0) 22%),
      linear-gradient(100deg, var(--navy-light) 0%, var(--navy-mid) 45%, var(--navy-deep) 100%);
  }
  .swatches {
    position: absolute; top: 0; left: 662px;
    display: flex; gap: 9px;
  }
  .swatch { width: 66px; height: 89px; }
  .swatch--yellow { background: var(--swatch-yellow); }
  .swatch--orange { background: var(--swatch-orange); }
  .swatch--red { background: var(--swatch-red); }
  .swatch--plum { background: var(--swatch-plum); }
  .swatch--sky { background: var(--swatch-sky); }
  .swatch--green { background: var(--swatch-green); }

  .badge {
    position: absolute; border-radius: 50%;
    display: flex; flex-direction: column; align-items: center; justify-content: center;
    text-align: center;
    font-family: "Ubuntu", sans-serif; font-weight: 700;
    line-height: 1.25;
  }
  .badge--experience {
    left: 39px; top: -16px; width: 200px; height: 200px;
    background: var(--badge-dark); font-size: 21px; letter-spacing: 0.5px;
  }
  .badge--experience .badge-big { font-size: 34px; line-height: 1.1; letter-spacing: 1px; }
  .badge--standard {
    left: 164px; top: 302px; width: 230px; height: 230px;
    background: var(--badge-slate); font-size: 23px; letter-spacing: 0.5px;
  }

  .info {
    position: absolute; left: 640px; width: 460px; text-align: center;
  }
  .info-heading {
    font-family: "Ubuntu", sans-serif; font-weight: 500;
    font-size: 24px; letter-spacing: 0.3px;
  }
  .info-body { font-size: 18px; line-height: 25px; }
  .services { top: 110px; }
  .contact { top: 232px; }
  .contact .info-body { line-height: 22px; }

  .brand-panel {
    position: absolute; left: 446px; top: 343px;
    width: 654px; height: 148px; background: var(--white);
    display: flex; flex-direction: column; justify-content: center;
    padding-left: 36px;
  }
  .brand-name {
    font-family: "Ubuntu", sans-serif; font-weight: 700;
    color: var(--brand-green); font-size: 50px; line-height: 1.05;
  }
</style>
</head>
<body>
  <main class="flyer">
    <div class="backdrop-photo" role="img" aria-label="Photo of open paint tins in black, yellow, red, cream and slate blue on a deep blue background"></div>

    <div class="swatches">
      <div class="swatch swatch--yellow"></div>
      <div class="swatch swatch--orange"></div>
      <div class="swatch swatch--red"></div>
      <div class="swatch swatch--plum"></div>
      <div class="swatch swatch--sky"></div>
      <div class="swatch swatch--green"></div>
    </div>

    <div class="badge badge--experience">
      <span>Over</span>
      <span class="badge-big">25 years</span>
      <span>experience</span>
    </div>

    <div class="badge badge--standard">
      <span>We set the</span>
      <span>standard for</span>
      <span>quality and</span>
      <span>service</span>
    </div>

    <section class="info services">
      <h2 class="info-heading">All Painting services offered:</h2>
      <p class="info-body">Interior, exterior, pressure washing, staing,<br>roof restoration, residential, commercial<br>and body corporate</p>
    </section>

    <section class="info contact">
      <h2 class="info-heading">Call for a free estimate:</h2>
      <p class="info-body">Dorian Velsher 0498153620<br>Dorianvelsher0@quillmail.com<br>brennardfinishcoatings.webnest.com.au</p>
    </section>

    <div class="brand-panel">
      <span class="brand-name">Brennard<br>Finish Coatings</span>
    </div>
  </main>
</body>
</html>
```